Kneadwell Points website re-design and

the academy of bodywork studies is ready for a new website. The current website is around 12 years old and it looks old. Luckily the clients is not against changing the colors so the new design does not have to use the current ugly green color scheme. Be creative! Make it pretty, modern and inviting. The current colors look like mold. Nobody likes mold. I have attached the logo asset file as well as a txt document that details the new website design parameters

1 page

```html
<!DOCTYPE html>
<html lang="en">
<head>
<meta charset="utf-8">
<title>Academy of Bodywork Studies – Kneadwell Points</title>
<link rel="stylesheet" href="https://fonts.googleapis.com/css2?family=Playfair+Display:wght@400;700&family=Mulish:wght@400;600;700&display=swap">
<style>
:root{
  --blue:#1a82d4;
  --blue-dark:#146bb0;
  --ink:#1b1b1b;
  --muted:#8a8a8a;
  --pale:#f3f7fb;
  --navy:#0d2f48;
  --footer:#1f2326;
  --line:#d8dde2;
  --white:#ffffff;
  --accent:#f2b632;
}
*{box-sizing:border-box;margin:0;padding:0}
html,body{width:1200px;height:2784px;overflow:hidden}
body{font-family:"Mulish",sans-serif;color:var(--ink);background:var(--white);position:relative}

/* top bar + nav */
.topbar{height:24px;background:var(--pale);position:relative}
.topbar .cart{position:absolute;right:130px;top:5px;font-size:10px;font-weight:700;display:flex;align-items:center;gap:5px}
.nav{height:59px;display:flex;align-items:center;justify-content:space-between;width:940px;margin:0 auto}
.brand{display:flex;align-items:center;gap:10px;color:var(--ink)}
.brand .mark{width:24px;height:24px;border-radius:50%;background:var(--ink);flex:none}
.brand .name{font-size:14px;line-height:16px;letter-spacing:1.5px;white-space:nowrap}
.menu{display:flex;align-items:center;gap:6px;font-size:12.5px}
.menu a{padding:7px 15px;color:var(--ink);text-decoration:none}
.menu a.active{background:var(--blue);color:var(--white)}
.btn-login{background:var(--blue);color:var(--white);border-radius:14px;padding:7px 22px;font-size:11.5px;font-weight:700;margin-left:6px}

/* hero */
.hero{height:417px;position:relative;background:linear-gradient(90deg,#f1f3f5 0%,#eceff1 45%,#e0d2c6 100%);overflow:hidden}
.hero-photo{position:absolute;left:470px;top:0;width:730px;height:417px;background:linear-gradient(100deg,rgba(236,239,241,1) 0%,#d9c2b0 35%,#c39a7f 60%,#a87a5f 85%,#8f6b57 100%)}
.hero-copy{position:absolute;left:130px;top:94px}
.hero-copy .kicker{font-size:20px}
.hero-copy h1{font-family:"Playfair Display",serif;font-weight:700;font-size:40px;line-height:49px;margin-top:10px}
.search{position:absolute;left:130px;top:258px;width:380px;height:128px;border:2px solid var(--blue);background:rgba(228,240,250,.92);text-align:center;padding-top:17px}
.search h3{font-size:13.5px;font-weight:700;letter-spacing:.3px}
.search .fields{display:flex;gap:4px;justify-content:center;margin-top:9px}
.search .field{background:var(--white);height:28px;font-size:9px;display:flex;align-items:center;justify-content:space-between;padding:0 8px;color:#444}
.search .go{width:307px;height:27px;margin:8px auto 0;background:var(--blue);color:var(--white);font-size:10.5px;font-weight:700;display:flex;align-items:center;justify-content:center}

/* section shared */
.section{position:relative}
.section h2{font-family:"Playfair Display",serif;font-weight:700;font-size:40px;text-align:center}
.arrow{position:absolute;width:38px;height:38px;border:1px solid #bfc5cb;border-radius:50%;background:var(--white);display:flex;align-items:center;justify-content:center}
.arrow.left{left:46px}.arrow.right{left:1116px}
.cards{display:flex;gap:20px;width:940px;margin:0 auto}
.card{width:220px;text-align:center}
.card .frame{height:168px;background:var(--white);border-radius:12px;box-shadow:0 1px 8px rgba(0,0,0,.12);display:flex;align-items:center;justify-content:center}
.card .title{font-family:"Playfair Display",serif;font-size:16.5px;margin-top:14px;line-height:21px}
.packages .title,.shop .title{white-space:nowrap}
.card .credit{font-size:10.5px;color:var(--muted);margin-top:5px}
.pill{display:inline-flex;align-items:center;gap:6px;background:var(--blue);color:var(--white);border-radius:18px;height:33px;padding:0 4px 0 17px;font-size:12px;margin-top:14px}
.pill .dot{width:25px;height:25px;border-radius:50%;background:var(--white);display:flex;align-items:center;justify-content:center}

.packages{height:449px;padding-top:50px}
.packages .cards{margin-top:26px}
.certs{height:467px;background:var(--pale);padding-top:57px}
.certs .cards{margin-top:19px}
.certs .frame{border-radius:12px 12px 0 0;box-shadow:none}
.certs .title{height:46px}
.certs .pill{margin-top:12px}
.cert-img{width:124px;height:94px;background:linear-gradient(135deg,#d8c9a6,#b89b6b);border:3px solid #8b6d44}

.shop{height:501px;padding-top:57px}
.shop .cards{margin-top:19px}
.shop .frame{height:236px;border-radius:0;box-shadow:none;border:1px solid #9aa0a6}
.book{width:110px;height:142px}
.shop .buttons{display:flex;gap:6px;justify-content:center;margin-top:13px}
.shop .btn{height:30px;width:95px;border-radius:15px;font-size:11px;display:flex;align-items:center;justify-content:center}
.btn.cart{background:var(--blue);color:var(--white)}
.btn.buy{background:var(--navy);color:var(--white)}

/* titles */
.titles{height:493px;background:linear-gradient(180deg,#0f3550,#0b2b42);color:var(--white);padding-top:38px}
.titles h2{color:var(--white)}
.title-cols{position:absolute;top:120px;left:0;width:1200px}
.title-cols ul{position:absolute;list-style:none;font-size:13.5px;line-height:26.7px;white-space:nowrap}
.title-cols li::before{content:"";display:inline-block;width:5px;height:5px;background:var(--accent);margin-right:5px;vertical-align:middle}
.btn-free{position:absolute;left:516px;top:416px;width:168px;height:34px;border-radius:17px;background:var(--blue);display:flex;align-items:center;justify-content:center;font-size:11.5px;font-weight:700;letter-spacing:.3px}

/* footer */
.footer{height:374px;background:var(--footer);color:var(--white);position:relative}
.footer .brand{position:absolute;left:130px;top:64px;color:var(--white)}
.footer .brand .mark{background:var(--white)}
.footer .brand .name{font-size:15px;line-height:18px}
.footer .login{position:absolute;left:131px;top:132px;background:var(--blue);border-radius:13px;padding:6px 20px;font-size:11px}
.divider{position:absolute;top:58px;width:2px;height:212px;background:#3a3f44}
.divider::before{content:"";position:absolute;top:0;left:0;width:2px;height:20px;background:var(--blue)}
.fcol{position:absolute;top:62px}
.fcol h4{font-family:"Playfair Display",serif;font-weight:700;color:var(--blue);font-size:17px}
.fcol ul{list-style:none;font-size:12px;line-height:24px;margin-top:12px}
.contact{display:flex;align-items:flex-start;gap:8px;font-size:12px;line-height:17px;margin-top:12px}
.contact .ic{width:29px;height:29px;border-radius:50%;background:var(--blue);display:flex;align-items:center;justify-content:center;flex:none}
.copy{position:absolute;top:312px;width:1200px;text-align:center;font-size:10.5px}
.copy span{color:var(--blue)}
</style>
</head>
<body>

<div class="topbar">
  <div class="cart"><svg width="11" height="12" viewBox="0 0 11 12"><path d="M1 3h9v8H1zM3.5 3V2a2 2 0 0 1 4 0v1" fill="none" stroke="#222" stroke-width="1.2"/></svg>My Cart</div>
</div>
<header class="nav">
  <div class="brand"><span class="mark"></span><span class="name">ACADEMY OF<br>BODYWORK STUDIES</span></div>
  <nav class="menu">
    <a class="active">Home</a><a>Courses</a><a>Guidelines</a><a>Faqs</a><a>Policies</a><a>Contact</a><a>About</a>
    <span class="btn-login">LOGIN</span>
  </nav>
</header>

<section class="hero">
  <div class="hero-photo" role="img" aria-label="Woman relaxing with a lily in her hair while receiving a back massage"></div>
  <div class="hero-copy">
    <p class="kicker">Committed to Excellence in</p>
    <h1>Massage Therapy<br>Continuing Education</h1>
  </div>
  <div class="search">
    <h3>SEARCH ONLINE COURSES</h3>
    <div class="fields">
      <div class="field" style="width:151px">Search By Keyword</div>
      <div class="field" style="width:152px">No Of CE Hours <svg width="8" height="5"><path d="M1 1l3 3 3-3" fill="none" stroke="#444"/></svg></div>
    </div>
    <div class="go">Search</div>
  </div>
</section>

<section class="section packages">
  <h2>Popular Packages</h2>
  <div class="arrow left" style="top:142px"><svg width="8" height="10"><path d="M6 1L2 5l4 4" fill="none" stroke="#222" stroke-width="1.4"/></svg></div>
  <div class="arrow right" style="top:142px"><svg width="8" height="10"><path d="M2 1l4 4-4 4" fill="none" stroke="#222" stroke-width="1.4"/></svg></div>
  <div class="cards">
    <div class="card"><div class="frame"><div role="img" aria-label="Green and blue price tags with cart icons" style="width:92px;height:70px;background:linear-gradient(90deg,#27b335 50%,#1f5be0 50%);border-radius:4px"></div></div>
      <p class="title">Customize Your Own Package</p><p class="credit">Credit Hours: 0</p>
      <span class="pill">View Details <span class="dot"><svg width="7" height="10"><path d="M1.5 1l4 4-4 4" fill="none" stroke="#1a82d4" stroke-width="1.5"/></svg></span></span></div>
    <div class="card"><div class="frame"><div role="img" aria-label="Red hundred points emblem" style="width:54px;height:36px;background:#e8283c;border-radius:6px"></div></div>
      <p class="title">100 CE Package</p><p class="credit">Credit Hours: 100</p>
      <span class="pill">View Details <span class="dot"><svg width="7" height="10"><path d="M1.5 1l4 4-4 4" fill="none" stroke="#1a82d4" stroke-width="1.5"/></svg></span></span></div>
    <div class="card"><div class="frame"><div role="img" aria-label="Red special offer seal" style="width:84px;height:84px;border-radius:50%;background:radial-gradient(circle,#e33 0%,#a10f14 100%)"></div></div>
      <p class="title">Board Certified Renewal,</p><p class="credit">Credit Hours: 24</p>
      <span class="pill">View Details <span class="dot"><svg width="7" height="10"><path d="M1.5 1l4 4-4 4" fill="none" stroke="#1a82d4" stroke-width="1.5"/></svg></span></span></div>
    <div class="card"><div class="frame"><div role="img" aria-label="Green discount tag" style="width:96px;height:60px;background:linear-gradient(135deg,#b8e08a,#7cbf4a);border-radius:10px"></div></div>
      <p class="title">Maryland Package</p><p class="credit">Credit Hours: 7</p>
      <span class="pill">View Details <span class="dot"><svg width="7" height="10"><path d="M1.5 1l4 4-4 4" fill="none" stroke="#1a82d4" stroke-width="1.5"/></svg></span></span></div>
  </div>
</section>

<section class="section certs">
  <h2>Certification</h2>
  <div class="arrow left" style="top:115px"><svg width="8" height="10"><path d="M6 1L2 5l4 4" fill="none" stroke="#222" stroke-width="1.4"/></svg></div>
  <div class="arrow right" style="top:115px"><svg width="8" height="10"><path d="M2 1l4 4-4 4" fill="none" stroke="#222" stroke-width="1.4"/></svg></div>
  <div class="cards">
    <div class="card"><div class="frame"><div class="cert-img" role="img" aria-label="Framed certificate of achievement"></div></div>
      <p class="title">Certified Fertility Massage Therapist</p>
      <span class="pill">View Details <span class="dot"><svg width="7" height="10"><path d="M1.5 1l4 4-4 4" fill="none" stroke="#1a82d4" stroke-width="1.5"/></svg></span></span></div>
    <div class="card"><div class="frame"><div class="cert-img" role="img" aria-label="Framed certificate of achievement"></div></div>
      <p class="title">Certified Infant Massage Therapist~Instructor</p>
      <span class="pill">View Details <span class="dot"><svg width="7" height="10"><path d="M1.5 1l4 4-4 4" fill="none" stroke="#1a82d4" stroke-width="1.5"/></svg></span></span></div>
    <div class="card"><div class="frame"><div class="cert-img" role="img" aria-label="Framed certificate of achievement"></div></div>
      <p class="title">Certified Massage Doula</p>
      <span class="pill">View Details <span class="dot"><svg width="7" height="10"><path d="M1.5 1l4 4-4 4" fill="none" stroke="#1a82d4" stroke-width="1.5"/></svg></span></span></div>
    <div class="card"><div class="frame"><div class="cert-img" role="img" aria-label="Framed certificate of achievement"></div></div>
      <p class="title">Certified Prenatal Massage Therapist</p>
      <span class="pill">View Details <span class="dot"><svg width="7" height="10"><path d="M1.5 1l4 4-4 4" fill="none" stroke="#1a82d4" stroke-width="1.5"/></svg></span></span></div>
  </div>
</section>

<section class="section shop">
  <h2>Shop Our Course</h2>
  <div class="arrow left" style="top:211px"><svg width="8" height="10"><path d="M6 1L2 5l4 4" fill="none" stroke="#222" stroke-width="1.4"/></svg></div>
  <div class="arrow right" style="top:211px"><svg width="8" height="10"><path d="M2 1l4 4-4 4" fill="none" stroke="#222" stroke-width="1.4"/></svg></div>
  <div class="cards">
    <div class="card"><div class="frame"><div class="book" role="img" aria-label="Book cover for a stretching anatomy course" style="background:linear-gradient(180deg,#3a2a22,#8a5a3c)"></div></div>
      <p class="title">Stretching Anatomy</p><p class="credit">Credit Hours: 14</p>
      <div class="buttons"><span class="btn cart">Add to Cart</span><span class="btn buy">Shop Now</span></div></div>
    <div class="card"><div class="frame"><div class="book" role="img" aria-label="Blue book cover for a fibromyalgia course" style="background:linear-gradient(180deg,#6fa6dc,#3f7fc6)"></div></div>
      <p class="title">Fibromyalgia</p><p class="credit">Credit Hours: 16</p>
      <div class="buttons"><span class="btn cart">Add to Cart</span><span class="btn buy">Shop Now</span></div></div>
    <div class="card"><div class="frame"><div class="book" role="img" aria-label="Book cover for a facilitated stretching course" style="background:linear-gradient(180deg,#4c6f96,#2e4561)"></div></div>
      <p class="title">Facilitated PNF Stretching</p><p class="credit">Credit Hours: 18</p>
      <div class="buttons"><span class="btn cart">Add to Cart</span><span class="btn buy">Shop Now</span></div></div>
    <div class="card"><div class="frame"><div class="book" role="img" aria-label="Book cover for a sports and exercise massage course" style="background:linear-gradient(180deg,#c8472a,#7c2a1a)"></div></div>
      <p class="title">Sports &amp; Exercise Massage</p><p class="credit">Credit Hours: 25</p>
      <div class="buttons"><span class="btn cart">Add to Cart</span><span class="btn buy">Shop Now</span></div></div>
  </div>
</section>

<section class="section titles">
  <h2>Available Course Titles</h2>
  <div class="title-cols">
    <ul style="left:130px">
      <li>Certified Fertility Massage Therapist</li><li>Certified Massage Doula</li><li>Customize Your Own Package</li><li>Anatomy Fascial Lines</li><li>Board Certified Renewal, Package 1</li><li>Board Certified Renewal, Package 3</li><li>Deep Tissue Therapy</li><li>Draping Your Client (Ethics Standard V)</li><li>Ethics - Communication</li><li>Ethics - Listening</li>
    </ul>
    <ul style="left:424px">
      <li>Facilitated PNF Stretching</li><li>Florida Laws &amp; Rules - 10 hours #20-308410</li><li>Florida Renewal 6 CE package - Laws, PME, Ethics</li><li>Human Trafficking Awareness and Prevention, 1 CE</li><li>Maryland Package</li><li>Orthopedic Massage for the Extremities</li><li>Pathology - Deep Vein Thrombosis</li><li>Pathology - Morton Foot Structure</li><li>Pathology - Sciatic Pain</li><li>Pathology - Varicose Veins</li>
    </ul>
    <ul style="left:791px">
      <li>Prenatal Massage Techniques (Step Two)</li><li>Reflexology for Feet and Hands</li><li>Research - Pregnancy and Labor Massage</li><li>Seven Mistakes Massage Therapists Make</li><li>Sports &amp; Exercise Massage</li><li>Certified Infant Massage Therapist~Instructor</li><li>Certified Prenatal Massage Therapist</li><li>100 CE Package</li><li>Aromatherapy for Massage</li><li>Board Certified Renewal, Package 2</li>
    </ul>
  </div>
  <div class="btn-free">VIEW ALL FREE COURSES</div>
</section>

<footer class="footer">
  <div class="brand"><span class="mark"></span><span class="name">ACADEMY OF<br>BODYWORK STUDIES</span></div>
  <span class="login">LOGIN</span>
  <div class="divider" style="left:400px"></div>
  <div class="divider" style="left:592px"></div>
  <div class="divider" style="left:897px"></div>
  <div class="fcol" style="left:450px">
    <h4>Quick Links</h4>
    <ul><li>Home</li><li>Courses</li><li>Guidelines</li><li>Faqs</li><li>Policies</li><li>Contact</li><li>About</li></ul>
  </div>
  <div class="fcol" style="left:642px">
    <h4>Contacts</h4>
    <div class="contact" style="margin-top:16px"><span class="ic"><svg width="11" height="14" viewBox="0 0 11 14"><path d="M5.5 0A5.5 5.5 0 0 0 0 5.5C0 9 5.5 14 5.5 14S11 9 11 5.5A5.5 5.5 0 0 0 5.5 0zm0 7.5a2 2 0 1 1 0-4 2 2 0 0 1 0 4z" fill="#fff"/></svg></span><span>15/B Lorem ipsum dolar sit amet<br>Florida 258K USA</span></div>
    <div class="contact" style="margin-top:26px"><span class="ic"><svg width="12" height="12" viewBox="0 0 12 12"><path d="M2.5 0.5l2 2.5-1.2 1.2a7 7 0 0 0 4.5 4.5L9 7.5l2.5 2L10 11.5C5 11.5 0.5 7 0.5 2z" fill="#fff"/></svg></span><span style="line-height:29px">555-014-2290</span></div>
    <div class="contact" style="margin-top:26px"><span class="ic"><svg width="12" height="9" viewBox="0 0 12 9"><rect width="12" height="9" rx="1" fill="#fff"/><path d="M0.5 0.8l5.5 4 5.5-4" fill="none" stroke="#1a82d4" stroke-width="1.2"/></svg></span><span style="line-height:29px">hello@bodyworkstudies.example</span></div>
  </div>
  <div class="fcol" style="left:936px">
    <h4>Courses</h4>
    <ul><li>Pregnancy / Doula</li><li>Florida Laws &amp; Packages</li><li>Research Courses</li></ul>
  </div>
  <p class="copy">Copyright © 2022 <span>Academy of Bodywork Studies</span>. All Rights Reserved.</p>
</footer>

</body>
</html>
```